Comedy Hypnotist Morlan T Show Poster

I need a poster that can send to clubs that book my show for them in turn to use to promote me/my show at their club. The poster needs to be fun and attractive, and to have a blank space at the bottom where the club(s) can add the details particular to their show. [You'll have seen these posters everywhere for bands etc.]

I'm not fussy about whether or not you use the colours from my website or any of my photos. But do capture at least the essence of the logo somewhere.

I am not like other hypnotists - I want to convey an image of amazing hilarious fun, that everyone can enjoy. [NO Watches, NO Chickens and NO Spirals]. My show is hilarious and clean.

I come across as a little geeky, and very professional. Not sleazy or creepy. But fun, professional and easy to deal with. The show is loud, buzzy and amazing. People literally laugh until they cry. I use great lighting and amazing sound to make it a real event. I aim to entertain everyone. I am never mean and don't pick on or exploit people. (Check the website for video links and more images as well as the crap posters I use now) www.morlant-shows.example.

Somehow I want people who see my poster to go - that looks like fun! Lets check it out. I would so totally go to that.

It's worth looking at the website and the youtube vid to get a feel for what I do. The pictures you'll see are colourful and active.

My logo is newish - I like it because it is simple, professional and elegant - and different from other hypnotists. In a way that is my main marketing angle - I am different from other hypnotists.

Posters should be international paper A3 size.

Target Market(s)

entertainment, comedy, hypnotist

Industry/Entity Type

Entertainment Industry

Font styles to use
Sans Serif

Requirements
Must have
• Space at the bottom (white space) for people to write the details of their event on.
• "www.morlant-shows.example" in case they want to look me up.
• "Comedy Hypnotist"
• "Morlan T"
Nice to have
• Simple and clean designs. You don't have to use the logo but if you reference it somehow that would be better so they tie together. I have included some studio photos of myself but these are not required for the poster. You can choose not to include any picture - they are there for if you want them for your design idea.
Should not have
• Spirals, Watches, Chickens

```html
<!DOCTYPE html>
<html lang="en">
<head>
<meta charset="utf-8">
<title>Comedy Hypnotist Morlan T – Show Poster</title>
<link rel="stylesheet" href="https://fonts.googleapis.com/css2?family=Anton&family=Montserrat:wght@400;700&family=Oswald:wght@700&display=swap">
<style>
  :root {
    --paper: #ffffff;
    --sage: #9bb49a;
    --sage-light: #c4d6c2;
    --sage-dark: #6f8c6f;
    --ink: #161616;
    --placeholder: #e2e3e6;
    --rating-green: #6cb33e;
    --photo-dark: #2b2b2b;
    --photo-light: #d9d6d2;
  }
  html, body {
    margin: 0;
    padding: 0;
    width: 849px;
    height: 1200px;
    overflow: hidden;
    background: var(--paper);
  }
  .poster {
    position: relative;
    width: 849px;
    height: 1200px;
    background: var(--paper);
    overflow: hidden;
  }
  .headline {
    position: absolute;
    inset: 0;
    width: 849px;
    height: 1200px;
  }
  .headline text {
    font-family: "Anton", "Oswald", sans-serif;
  }
  .performer-name {
    fill: var(--ink);
  }
  .website {
    position: absolute;
    left: 408px;
    top: 928px;
    margin: 0;
    font-family: "Montserrat", sans-serif;
    font-size: 19px;
    letter-spacing: 2px;
    color: var(--ink);
    white-space: nowrap;
  }
  .website strong { font-weight: 700; }
  .performer-photo {
    position: absolute;
    left: 0;
    top: 866px;
    width: 282px;
    height: 334px;
    background: linear-gradient(180deg, var(--photo-light) 0%, #bdb8b2 18%, var(--photo-dark) 36%, #1f1f1f 100%);
    border-radius: 110px 110px 0 0;
  }
  .rating-badge {
    position: absolute;
    left: 208px;
    top: 990px;
    width: 70px;
    height: 70px;
    border-radius: 10px;
    background: var(--rating-green);
  }
  .event-details {
    position: absolute;
    left: 300px;
    top: 985px;
    width: 470px;
  }
  .event-details text {
    font-family: "Oswald", sans-serif;
    font-weight: 700;
    fill: var(--placeholder);
  }
</style>
</head>
<body>
<main class="poster">
  <svg class="headline" viewBox="0 0 849 1200" aria-label="Comedy Hypnotist Morlan T">
    <defs>
      <linearGradient id="sage-fill" x1="0" y1="0" x2="0" y2="1">
        <stop offset="0" stop-color="var(--sage)"/>
        <stop offset="0.55" stop-color="var(--sage-light)"/>
        <stop offset="1" stop-color="var(--sage-dark)"/>
      </linearGradient>
    </defs>
    <text class="show-type" x="66" y="400" font-size="380" textLength="712" lengthAdjust="spacingAndGlyphs" fill="url(#sage-fill)">COMEDY</text>
    <text class="show-type" x="64" y="650" font-size="284" textLength="722" lengthAdjust="spacingAndGlyphs" fill="url(#sage-fill)">HYPNOTIST</text>
    <text class="performer-name" x="64" y="855" font-size="222" textLength="772" lengthAdjust="spacingAndGlyphs">MORLAN T</text>
  </svg>

  <p class="website">www.<strong>morlant-shows</strong>.example</p>

  <div class="performer-photo" role="img" aria-label="Studio photo of the performer in glasses, white shirt and black waistcoat, smiling and holding up a rating card"></div>
  <div class="rating-badge" role="img" aria-label="Family rating badge"></div>

  <svg class="event-details" viewBox="0 0 470 170" width="470" height="170" aria-label="Space for the other stores">
    <text x="0" y="78" font-size="92" textLength="465" lengthAdjust="spacingAndGlyphs">SPACE FOR THE</text>
    <text x="0" y="166" font-size="92" textLength="465" lengthAdjust="spacingAndGlyphs">OTHER STORES</text>
  </svg>
</main>
</body>
</html>
```